StartFirmo.eu - need to polish our homepage (layout only)

We run a website project (http://cz.StartFirmo.eu) enabling free company formations via the Internet.

We now do complete redesign of the website which is almost ready but we still cannot get to proper shape of the homepage and we kindly ask you to participate on finalisation of this.

What we have now:
- design of sub-pages (see attached as NewSubPage design)

What must be preserved on homepage:
- upper horizontal menu and everything above it (logo, sign in button etc.)
- bottom quick navigation menu

What we would like to have (see attached HPSketch):
- unlike current homepage (http://cz.StartFirmo.eu) some introductory section just below the upper horizontal menu which will contain catching words/references

- more detailed website description and left navigation below this introductory section

- right banners stating amount of statutory fees and costs for registered office (if one chooses so)

- section for news

Thank you in advance for your proposals. In case of any queries please let us know.
Updates

Hello designers,

Many thanks for your first proposals, just.two general comments before I comment on particular designs:

1) We will probably want that the website does NOT include images of people but rather keep it as purely informative. The reason is that as we provide free service users often take us as sort of governmental agency and for such it is not very common here to have such type of public images on the website.

2) We will have 2 banners positions for our partners, one 970x200 leaderboard on the top of webpage and one left square below left navigation. You do not need to include them in your proposals, I am just mentioning this that this space must be left free for this purpose.

Many thanks for your effort so far, I will also comment separately on your particular designs.

Lukas

Requirements
Nice to have
• - you may consider substituting bullets in short catching sentences in introductory section by some icons expressing nature of the sentence

```html
<!DOCTYPE html>
<html lang="en">
<head>
<meta charset="utf-8">
<title>StartFirmo.eu – Free company formations online</title>
<link href="https://fonts.googleapis.com/css2?family=Arimo:wght@400;700&display=swap" rel="stylesheet">
<style>
:root{
  --ad-yellow:#fdca44;
  --sky:#a9d6f7;
  --navy:#0b4f93;
  --deep:#08427c;
  --footer:#0b5599;
  --bright:#1a70c8;
  --ink:#111;
  --text-blue:#1266b5;
  --grey-box:#bdbdbd;
  --white:#fff;
}
*{box-sizing:border-box;margin:0;padding:0}
html,body{width:728px;height:1200px;overflow:hidden}
body{font-family:"Arimo",Arial,sans-serif;color:var(--ink);background:var(--white);position:relative}
.abs{position:absolute}
a{color:inherit;text-decoration:none}

.ad{background:var(--ad-yellow);color:var(--text-blue);display:flex;align-items:center;justify-content:center;font-size:18px}
.ad-top{left:0;top:0;width:728px;height:148px}
.ad-side{left:43px;top:801px;width:192px;height:193px}

.header{left:0;top:148px;width:728px;height:86px;background:var(--sky)}
.brand{left:24px;top:30px;display:flex;align-items:center;gap:8px;font-size:27px;font-weight:700;color:var(--navy)}
.brand-mark{width:30px;height:30px;background:var(--navy)}
.contact{right:23px;top:9px;text-align:right;font-size:11.5px;color:var(--navy);line-height:16px}
.contact .phone{font-size:12.5px}
.search{right:23px;top:61px;display:flex;gap:2px}
.search span{display:block;height:13px;font-size:7px;line-height:13px;padding:0 5px}
.search .field{width:108px;background:var(--white);color:var(--text-blue)}
.search .go{width:21px;background:var(--navy);color:var(--white);text-align:center}

.mainnav{left:0;top:234px;width:728px;height:30px;background:var(--navy);color:var(--white);font-size:11.5px}
.mainnav ul{list-style:none;display:flex;justify-content:center;padding-top:9px;gap:0}
.mainnav li+li::before{content:"|";margin:0 12px}
.flag{left:684px;top:8px}

.panel{border:1px solid var(--text-blue);border-radius:12px}
.sidenav{left:21px;top:274px;width:173px;height:247px}
.sidenav ul{list-style:none;padding:19px 0 0 16px;font-size:13px;line-height:23px}
.badges{left:20px;top:170px;display:flex;gap:12px}
.badges span{width:58px;height:58px;border-radius:50%;background:#e6eef7}

.intro{left:206px;top:274px;width:318px}
.sublinks{font-size:11px;text-align:center;padding-top:9px;margin-left:-4px}
.sublinks span{margin:0 8px}
.intro h1{font-weight:400;font-size:20px;color:var(--text-blue);margin:19px 0 0 2px}
.perks{list-style:none;margin:13px 0 0 22px;font-size:14.5px;line-height:22.5px}
.perks li{display:flex;align-items:center;gap:9px}
.count{left:9px;top:208px;display:flex;align-items:center;font-size:13px;gap:10px}
.count b{display:block;width:100px;height:21px;background:var(--grey-box);font-weight:400;font-size:17px;text-align:center;line-height:21px}

.offers{left:534px;top:274px;width:173px;height:247px;color:var(--navy);font-size:9.5px}
.offers h3{font-weight:400;font-size:12.5px;color:var(--text-blue);margin:21px 0 0 11px;line-height:14px}
.offers p{margin-left:21px;color:var(--ink);line-height:18px}
.offers .list{margin-top:7px}
.offers .cta{position:absolute;left:0;right:0;top:200px;text-align:center;font-size:11px;color:var(--text-blue)}
.offers .cta strong{display:block;font-weight:400;font-size:14px}

.why-title{left:0;top:546px;width:728px;text-align:center;font-size:27px;color:var(--text-blue);font-weight:400}
.why{top:603px;font-size:10.4px;line-height:13.6px;width:304px}
.why p{margin-bottom:14px;text-indent:0}
.why p::before{content:"\2714";margin:0 6px 0 0;font-size:12px}
.why-left{left:54px}
.why-right{left:385px;width:316px}

.box{top:801px;width:192px;height:193px;background:var(--navy);color:var(--white)}
.box h2{background:var(--bright);font-weight:400;font-size:16px;text-align:center;height:26px;line-height:26px}
.news{left:268px}
.testimonials{left:493px}
.news article{margin:4px 0 0 18px;width:165px;font-size:10px;line-height:10.5px}
.news article+article{margin-top:11px}
.news strong{display:block}
.more{position:absolute;right:18px;bottom:4px;font-size:9px}
.testimonials article{margin:5px 0 0 17px;width:168px;font-size:6.8px;line-height:9.6px}
.testimonials h4{font-weight:400;font-size:10.5px;line-height:14px}
.testimonials article+article{margin-top:6px}

.footer{left:0;top:1008px;width:728px;height:145px;background:var(--footer);color:var(--white)}
.footer section{position:absolute;top:22px}
.footer h5{font-weight:400;font-size:14px;margin-bottom:16px}
.footer ul{list-style:none;font-size:11px;line-height:15px;padding-left:20px}
.footer li::before{content:"> "}
.legal{left:0;top:1153px;width:728px;height:47px;background:var(--deep);color:var(--white);font-size:11px;text-align:center;line-height:43px}
.legal span{margin:0 12px}
</style>
</head>
<body>

<div class="abs ad ad-top">BANNER AD</div>

<header class="abs header">
  <div class="abs brand"><span class="brand-mark"></span>StartFirmo.eu</div>
  <div class="abs contact">
    <div class="phone">220 555 018</div>
    <div>info@StartFirmo.eu</div>
    <div><a href="#">Log in</a> &nbsp; | &nbsp; <a href="#">Sign up</a></div>
  </div>
  <div class="abs search"><span class="field">SEARCH</span><span class="go">GO</span></div>
</header>

<nav class="abs mainnav">
  <ul><li>HOME</li><li>ABOUT US</li><li>FORMS</li><li>HOW IT WORKS</li><li>CONTACT US</li></ul>
  <svg class="abs flag" width="21" height="14" viewBox="0 0 21 14"><rect width="21" height="7" fill="#fff"/><rect y="7" width="21" height="7" fill="#d7141a"/><path d="M0 0L10 7L0 14Z" fill="#11457e"/></svg>
</nav>

<aside class="abs panel sidenav">
  <ul><li>HOW IT WORKS</li><li>BEFORE BEGINNING</li><li>FORM YOUR COMPANY</li><li>CHECK REGISTRATION</li><li>FAQ</li><li>CONTACTS</li></ul>
  <div class="abs badges"><span role="img" aria-label="Award badge"></span><span role="img" aria-label="Chamber membership badge"></span></div>
</aside>

<section class="abs intro">
  <div class="sublinks"><span>S.R.O. Formation</span>|<span>Trade License</span>|<span>A.S. Formation</span></div>
  <h1>FREE Company formations online</h1>
  <ul class="perks">
    <li><svg width="17" height="17" viewBox="0 0 17 17" fill="var(--bright)"><path d="M8.5 0L12 3.5L8.5 7L5 3.5Z"/><path d="M8.5 10L12 13.5L8.5 17L5 13.5Z"/><path d="M3.5 5L7 8.5L3.5 12L0 8.5Z"/><path d="M13.5 5L17 8.5L13.5 12L10 8.5Z"/></svg>Pay statutory registration fees ONLY</li>
    <li><svg width="17" height="17" viewBox="0 0 17 17" fill="var(--bright)"><path d="M8.5 0L12 3.5L8.5 7L5 3.5Z"/><path d="M8.5 10L12 13.5L8.5 17L5 13.5Z"/><path d="M3.5 5L7 8.5L3.5 12L0 8.5Z"/><path d="M13.5 5L17 8.5L13.5 12L10 8.5Z"/></svg>NO need to attend to State Authorities</li>
    <li><svg width="17" height="17" viewBox="0 0 17 17" fill="var(--bright)"><path d="M8.5 0L12 3.5L8.5 7L5 3.5Z"/><path d="M8.5 10L12 13.5L8.5 17L5 13.5Z"/><path d="M3.5 5L7 8.5L3.5 12L0 8.5Z"/><path d="M13.5 5L17 8.5L13.5 12L10 8.5Z"/></svg>Registered capital from CZK 1</li>
    <li><svg width="17" height="17" viewBox="0 0 17 17" fill="var(--bright)"><path d="M8.5 0L12 3.5L8.5 7L5 3.5Z"/><path d="M8.5 10L12 13.5L8.5 17L5 13.5Z"/><path d="M3.5 5L7 8.5L3.5 12L0 8.5Z"/><path d="M13.5 5L17 8.5L13.5 12L10 8.5Z"/></svg>Company formed in 3-5 days</li>
  </ul>
  <div class="abs count">REGISTERED FIRMS TO DATE <b>4345</b></div>
</section>

<aside class="abs panel offers">
  <h3>STATUTORY COST ONLY,<br>NO COMMITMENTS</h3>
  <div class="list"><p>S.R..O. formation from CZK 13,500</p><p>ZL formation from CZK 1,000</p></div>
  <h3 style="margin-top:24px">NEED REGISTERED OFFICE?</h3>
  <div class="list"><p>PRAGUE &nbsp;from CZK 216 / Month</p><p>OSTRAVA from CZK 436 / Month</p></div>
  <div class="cta">UNBINDING REGISTRATION<strong>TRY IT NOW!</strong></div>
</aside>

<h2 class="abs why-title">Why StartFirmo.eu</h2>
<div class="abs why why-left">
  <p>The only system in the Czech Republic enabling the complex formation of new companies online through the Internet, without complicated administration, running around state authorities or visits of law firms.</p>
  <p>Free of charge handling with the payment of statutory registration fees only. &nbsp;&nbsp;&nbsp;&nbsp;Save 60-80% of costs in comparison with the formation of companies through a law firm or the purchase of a ready-made company.</p>
  <p>Short registration process, all documentation is generated automatically online and the registration is completed in short periods (usually 10-14 business days).</p>
</div>
<div class="abs why why-right">
  <p>Formation of new company with no trading history or transferred from third parties. No risk of potential hidden liabilities or previous records in the Company Register as in case of ready-made (shelf) companies.</p>
  <p>Simple and user-friendly online registration form enabling tailor-made company formation for each user.</p>
  <p>Guarantee of professional legal support and helpline during the whole course of the company's registration with 100% guarantee of registration in the Company Register.</p>
  <p>Possibility of further services to the new firm's business.</p>
</div>

<div class="abs ad ad-side">BANNER AD</div>

<section class="abs box news">
  <h2>NEWS</h2>
  <article>30. 09. 2011<strong>Applies to The Startups of the Year Awards</strong>Startups of the Year 2011 is a new competition, designated for starting entrepreneurs where va...</article>
  <article>15. 08. 2011<strong>The change of court fees for registrations in the Czech Company Register</strong>As of 1.9.2011, the change to statutory court fees will become effective for the registration o...</article>
  <a class="more" href="#">READ MORE &gt;</a>
</section>

<section class="abs box testimonials">
  <h2>TESTIMONIALS</h2>
  <article><h4>Name of Company</h4>"Lorem ipsum dolor sit amet, consectetur adipisicing elit, sed do eiusmod tempor incididunt ut labore et dolore magna aliqua. Ut enim ad minim veniam, quis nostrud exercitation ullamco laboris nisi ut aliquip ex ea commodo consequat.</article>
  <article><h4>Name of Company</h4>"Lorem ipsum dolor sit amet, consectetur adipisicing elit, sed do eiusmod tempor incididunt ut labore et dolore magna aliqua. Ut enim ad minim veniam, quis nostrud exercitation ullamco laboris nisi ut aliquip ex ea commodo consequat.</article>
  <a class="more" href="#">READ MORE &gt;</a>
</section>

<footer class="abs footer">
  <section style="left:59px"><h5>Form company</h5><ul><li>S.R.O.</li><li>Trade License</li></ul></section>
  <section style="left:247px"><h5>Client Zone</h5><ul><li>My Registration</li><li>Check Registration</li><li>My Profile</li></ul></section>
  <section style="left:421px"><h5>StartFirmo.eu</h5><ul><li>How it works</li><li>Before beginning</li><li>Business conditions</li><li>Affiliate program</li></ul></section>
  <section style="left:601px"><h5>Support</h5><ul><li>Contact</li><li>FAQ</li></ul></section>
</footer>
<div class="abs legal">Copyright StartFirmo.eu &nbsp;2014<span>|</span>Privacy Statement<span>|</span>Terms of Use</div>

</body>
</html>
```